Broschüre
Zielgruppe
Wir sind ein Projekt-Zusammenschluss aus zwei Firmen im Bereich Fahrzeugeinrichtungen/ Fahrzeugbau und planen eine gemeinsame Vertriebskampagne. Wir vertreiben und montieren in den eigenen Werkstätten Fahrzeugeinrichtungs-Systeme der Marke Kalvera (Marktführer) für Handwerker, Behörden und Versorger. Die Zielgruppe unserer Vertriebskampagne sind vorrangig Nutzfahrzeugverkäufer und Handwerker.
Die Broschüre sollen jeweils im CD der Firmen Wolter und Lindt gestaltet werden - nachrangig sollen Partner der Firmen Wolter und Lindt mit angegeben werden, wie zum Beispiel Autohäuser.
Aufgabenstellung
Wir beabsichtigen eine 8-seitige Broschüre im DIN A4-Format mit folgenden Inhalten:
- Vorstellung des Produktes
- Angebote (standardisierte Fahrzeugeinrichtungssysteme )
- Basic-Variante (eher spartanisch) und Pro-Variante (Allrounder - hohe Funktionalität)
- jeweils für kleine und mittlere Transporter
In Summe werden es ca. 10 Einrichtungssysteme (jeweils 5 Stk. für kleine und 5 Stk. für mittlere Transporter)
Text in ArialNarrow

```html
<!DOCTYPE html>
<html lang="de">
<head>
<meta charset="utf-8">
<title>Broschüre – Angebot für kleine Transporter</title>
<link href="https://fonts.googleapis.com/css2?family=Roboto+Condensed:wght@300;400;700&display=swap" rel="stylesheet">
<style>
  :root{
    --bg:#e4e4e4;
    --paper:#ffffff;
    --blue:#1e88d0;
    --blue-deep:#0f5aa6;
    --ink:#4a4a4a;
    --text:#555555;
    --dark:#4b4b4b;
    --photo-a:#5a73b0;
    --photo-b:#9aa8cf;
    --wall-a:#8e9297;
    --wall-b:#c6c8cb;
  }
  *{margin:0;padding:0;box-sizing:border-box}
  html,body{width:1200px;height:1200px;overflow:hidden;background:var(--bg)}
  body{font-family:"Roboto Condensed",sans-serif;position:relative}
  .spread{position:absolute;left:40px;top:195px;width:1120px;height:810px;display:flex;box-shadow:0 18px 40px rgba(0,0,0,.18)}
  .page{position:relative;width:560px;height:810px;background:var(--paper);overflow:hidden}
  .page--left{background:linear-gradient(90deg,#fff 80%,#ececec 100%)}
  .page--right{background:linear-gradient(90deg,#ececec 0%,#fff 12%)}
  .title-band{position:absolute;left:0;top:0;width:470px;height:118px}
  .title{position:absolute;left:58px;top:26px;color:#fff;font-weight:700;font-size:31px;line-height:37px}
  .section{position:absolute;left:58px;width:378px}
  .section h2{font-weight:700;font-size:25px;color:var(--ink);line-height:1}
  .rule{display:block;width:54px;height:3px;background:var(--dark);margin:20px 0 22px}
  .section p{font-weight:300;font-size:11.6px;line-height:14.8px;color:var(--text);text-align:justify;margin-bottom:13px}
  .pagenum{position:absolute;bottom:12px;font-size:11px;font-weight:300}
  .pagenum--left{left:19px;color:var(--blue)}
  .pagenum--right{right:19px;color:#fff}
  .divider{position:absolute;left:0;top:348px;width:560px;height:36px}
  .accessory-panel{position:absolute;left:0;top:383px;width:560px;height:427px;background:linear-gradient(135deg,var(--blue) 0%,var(--blue-deep) 100%)}
  .accessory-panel h3{position:absolute;left:62px;top:32px;color:#fff;font-weight:700;font-size:21px}
  .tile{position:absolute;width:184px;height:146px;overflow:hidden}
  .tile--floor{background:linear-gradient(160deg,var(--photo-b) 0%,var(--photo-a) 60%,#7c8fc2 100%)}
  .tile--wall{background:linear-gradient(180deg,var(--wall-b) 0%,var(--wall-a) 100%)}
  .tile-label{position:absolute;left:0;bottom:0;width:150px;height:28px;background:linear-gradient(90deg,rgba(60,60,60,.85),rgba(60,60,60,.55));clip-path:polygon(0 0,82% 0,100% 100%,0 100%);color:#fff;font-weight:700;font-size:12.5px;line-height:28px;padding-left:8px}
</style>
</head>
<body>
<div class="spread">
  <section class="page page--left">
    <svg class="title-band" viewBox="0 0 470 118" aria-hidden="true">
      <defs><linearGradient id="bandGrad" x1="0" x2="1"><stop offset="0" stop-color="#1e88d0"/><stop offset="1" stop-color="#2b97dc"/></linearGradient></defs>
      <polygon points="6,10 470,0 414,118 6,122" fill="url(#bandGrad)"/>
    </svg>
    <h1 class="title">Angebot für<br>kleine Transporter</h1>

    <div class="section" style="top:168px">
      <h2>Basic-Variante</h2>
      <span class="rule"></span>
      <p>Dein Fahrzeug ist häufig der erste Eindruck, den ein Kunde von dir gewinnt und somit die mobile Visitenkarte deines Unternehmens. Durch ein aufgeräumtes und gut sortiertes Fahrzeug unterstreichst du deine Kompetenz. Gerne unterstützen wir dich dabei die Arbeitsabläufe rund um dein Fahrzeug zu optimieren und planen individuelle Konzepte mit dem Fokus auf die alltägliche Arbeitserleichterung.</p>
      <p>Unser Einrichtungssystem Kalvera Rastera 4 bietet einen äußerst flexiblen Aufbau. Im Standard kann die Einrichtungshöhe im Rastermaß von 17 mm an die Fahrzeugsilhouette bzw. an den Kundenbedarf angepasst werden. Durch vier unterschiedliche Tiefen und fünf Breiten können auch Sonderlösungen mit Standard- Artikeln abgebildet werden.</p>
    </div>

    <div class="section" style="top:458px">
      <h2>Pro-Variante</h2>
      <span class="rule"></span>
      <p>Dein Fahrzeug ist häufig der erste Eindruck, den ein Kunde von dir gewinnt und somit die mobile Visitenkarte deines Unternehmens. Durch ein aufgeräumtes und gut sortiertes Fahrzeug unterstreichst du deine Kompetenz. Gerne unterstützen wir dich dabei die Arbeitsabläufe rund um dein Fahrzeug zu optimieren und planen individuelle Konzepte mit dem Fokus auf die alltägliche Arbeitserleichterung.</p>
      <p>Unser Einrichtungssystem Kalvera Rastera 4 bietet einen äußerst flexiblen Aufbau. Im Standard kann die Einrichtungshöhe im Rastermaß von 17 mm an die Fahrzeugsilhouette bzw. an den Kundenbedarf angepasst werden. Durch vier unterschiedliche Tiefen und fünf Breiten können auch Sonderlösungen mit Standard- Artikeln abgebildet werden.</p>
    </div>
    <span class="pagenum pagenum--left">02</span>
  </section>

  <section class="page page--right">
    <div class="section" style="top:64px;left:62px">
      <h2>Unterflur-Variante</h2>
      <span class="rule"></span>
      <p>Dein Fahrzeug ist häufig der erste Eindruck, den ein Kunde von dir gewinnt und somit die mobile Visitenkarte deines Unternehmens. Durch ein aufgeräumtes und gut sortiertes Fahrzeug unterstreichst du deine Kompetenz. Gerne unterstützen wir dich dabei die Arbeitsabläufe rund um dein Fahrzeug zu optimieren und planen individuelle Konzepte mit dem Fokus auf die alltägliche Arbeitserleichterung.</p>
      <p>Unser Einrichtungssystem Kalvera Rastera 4 bietet einen äußerst flexiblen Aufbau. Im Standard kann die Einrichtungshöhe im Rastermaß von 17 mm an die Fahrzeugsilhouette bzw. an den Kundenbedarf angepasst werden. Durch vier unterschiedliche Tiefen und fünf Breiten können auch Sonderlösungen mit Standard- Artikeln abgebildet werden.</p>
    </div>

    <svg class="divider" viewBox="0 0 560 36" aria-hidden="true">
      <polygon points="190,0 560,0 560,36 168,36" fill="#4b4b4b"/>
    </svg>

    <div class="accessory-panel">
      <h3>Das Zubehör</h3>
      <div class="tile tile--floor" style="left:62px;top:84px" role="img" aria-label="Foto: Bodenplatte mit Zurrschienen im Laderaum">
        <span class="tile-label">Bodenplatte</span>
      </div>
      <div class="tile tile--wall" style="left:281px;top:84px" role="img" aria-label="Foto: Seitenwandverkleidung im Laderaum">
        <span class="tile-label">Seitenwandverkleidung</span>
      </div>
      <div class="tile tile--floor" style="left:62px;top:239px" role="img" aria-label="Foto: Be- und Entlüftung im Fahrzeug">
        <span class="tile-label">Be-und Entlüftung</span>
      </div>
      <div class="tile tile--floor" style="left:281px;top:239px" role="img" aria-label="Foto: Beleuchtung im Laderaum">
        <span class="tile-label">Beleuchtung</span>
      </div>
    </div>
    <span class="pagenum pagenum--right">03</span>
  </section>
</div>
</body>
</html>
```